Social Media Tool / Marketing Tool homepage design

We need a design template for a website to promote a web based technology / service. The product provide companies with a tools to generate business from social media web site.

We would like a homepage designed and an inner page of the site. This can be a contact us page or a sign up screen... Would also be good to have a design for the blog page of the site and static page i.e affiliates or advertiser page.

The feel of the site should reflect the fact that this is a social media tool but should not be too casual as we will have business clients so a blend between informal, practical and should communicate to business people (professional marketers)

Site should look friendly, thinking rounded edges rather than squared.

We have included logo design and like the idea of using the haxagonal shapes on the background in some way... Also included link to black on black design mock up that's not right as it's too heavy and does not appeal to any of the women we have shown it to. (50% of our audience)

http://mockups.brindlevault-studio.example/ORB/showcase/html/mockup3.html

http://mockups.brindlevault-studio.example/ORB/showcase/html/mockup1_2.html

http://mockups.brindlevault-studio.example/ORB/showcase/html/inner-page1.html

Above link to design that's not right. The taxonomy is right just not the black on black design. We are happy to use black but not black on a black background.

Please consider that we have 4 user types we are trying to sell to on this page hence the 4 blocks on the homepage. Feel free to interparate this how you will could be good as hexagons? or blocks??

Have attached a powerpoint of site pages please take homepage and dummy content and sign up / form page or contact page.

I have also attached logos please only use logo with one coloured hexagon the other file (logo) does not have the hexagon coloured but does include a set of icons that could also be used.

logo font = Metrostyle extended

Target Market(s)

Young professional marketers at bluechip businesses. User of social media sites like pormbly / quillnest and chirvo.

Industry/Entity Type

Business

Requirements
Must have
• should include pormbly, chirvo and quillnest icons (these will link to our profiles on these sites) Should feel friendly yet established, should feel social as this is a tool to market via social media. rounded edges / corners.
Should not have
• not old style fonts not fonts like times roman .. no squared (hard) corners.

```html
<!DOCTYPE html>
<html lang="en">
<head>
<meta charset="utf-8">
<title>Orbametric – Advocacy Marketing Platform</title>
<link href="https://fonts.googleapis.com/css2?family=Bebas+Neue&family=Montserrat:wght@400;600;700&family=Arimo:wght@400;700&display=swap" rel="stylesheet">
<style>
:root{
  --black:#000;
  --ink:#111;
  --orange:#f15a22;
  --orange-dark:#d8430f;
  --grey:#666;
  --grey-light:#7a7a7a;
  --field:#8a8a8a;
  --white:#fff;
  --badge:#e6e6e6;
}
*{box-sizing:border-box;margin:0;padding:0}
html,body{width:1200px;height:768px;overflow:hidden;background:var(--white)}
body{position:relative;font-family:"Arimo",Arial,sans-serif;color:var(--ink)}
.abs{position:absolute}

/* header */
.topbar{left:0;top:0;width:1200px;height:58px;background:var(--black)}
.backdrop-pattern{left:30px;top:58px;width:320px;height:190px;background:radial-gradient(ellipse at 40% 20%,#f3f3f3 0%,rgba(255,255,255,0) 70%)}
.brand-tab{left:131px;top:0;width:89px;height:87px;background:#1a1a1a;border-radius:0 0 8px 8px;box-shadow:0 3px 6px rgba(0,0,0,.35)}
.brand-name{left:238px;top:14px;font-family:"Montserrat",sans-serif;font-weight:700;font-size:25px;color:var(--white);letter-spacing:.5px}
.login-field{top:19px;height:23px;background:var(--field);border-radius:4px;border:1px solid #9a9a9a;color:#bdbdbd;font-size:11px;padding:4px 9px}
.login-field.member{left:670px;width:153px}
.login-field.password{left:833px;width:152px}
.login-link{left:1002px;top:17px;font-family:"Bebas Neue",sans-serif;font-size:22px;color:var(--orange);letter-spacing:.5px}

/* nav */
.nav{left:0;top:52px;width:1200px;height:46px}
.nav a{position:absolute;top:18px;font-family:"Bebas Neue",sans-serif;font-size:21px;color:#333;text-decoration:none;letter-spacing:.6px}
.nav a.active{top:0;left:503px;width:62px;height:45px;background:#111;color:var(--white);border-radius:0 0 6px 6px;text-align:center;padding-top:17px;box-shadow:0 2px 4px rgba(0,0,0,.3)}

/* hero */
.hero-mark{left:198px;top:100px;width:106px;height:118px;background:linear-gradient(160deg,#fde3d8,#fbd0bf);border-radius:12px}
.hero-kicker{left:323px;top:128px;font-family:"Bebas Neue",sans-serif;font-size:28px;color:var(--orange);letter-spacing:.4px;line-height:1}
.hero-title{left:319px;top:151px;font-family:"Bebas Neue",sans-serif;font-weight:400;font-size:46px;color:var(--black);letter-spacing:1.5px;line-height:1;white-space:nowrap}
.btn-subscribe{left:865px;top:141px;width:204px;height:47px;border-radius:5px;background:linear-gradient(#f26a30,var(--orange-dark));font-family:"Bebas Neue",sans-serif;font-size:22px;line-height:19px;color:var(--white);padding:6px 0 0 22px;letter-spacing:.6px}
.chev{position:absolute;right:12px;top:0;height:100%}

/* audience cards */
.card{width:234px;height:184px;background:var(--black);border-radius:5px;box-shadow:0 1px 3px rgba(0,0,0,.4)}
.card-head{position:absolute;left:0;top:0;width:100%;height:56px;border-radius:5px 5px 0 0;background:linear-gradient(#3a3a3a,#1c1c1c 70%,#000)}
.card-icon{position:absolute;left:0;top:0;width:65px;height:56px;background:#050505;border-radius:5px 0 0 0;display:flex;align-items:center;justify-content:center}
.card-title{position:absolute;left:77px;top:17px;font-family:"Montserrat",sans-serif;font-size:18.5px;color:var(--white);letter-spacing:1.1px}
.card ul{position:absolute;left:15px;top:70px;width:205px;list-style:none;color:var(--white);font-size:12.5px;line-height:13px}
.card li{margin-bottom:11px}
.btn-register{position:absolute;left:37px;bottom:-15px;width:150px;height:34px;border-radius:3px;background:linear-gradient(#f26a30,var(--orange-dark));font-family:"Bebas Neue",sans-serif;font-size:22px;color:var(--white);padding:6px 0 0 16px;letter-spacing:.5px}
.btn-register .chev{right:14px}

/* intro column */
.intro-kicker{left:677px;top:242px;font-family:"Montserrat",sans-serif;font-weight:600;font-size:18px;line-height:18px;color:var(--black)}
.intro-head{left:677px;top:261px;font-family:"Montserrat",sans-serif;font-weight:600;font-size:29px;line-height:24px;color:var(--orange);white-space:nowrap}
.intro-copy{left:681px;top:318px;width:370px;font-size:17px;line-height:24px;color:var(--grey)}
.intro-copy em{color:var(--orange)}
.benefit{font-size:13px;line-height:18px;color:var(--black);padding-left:30px}
.benefit svg{position:absolute;left:5px;top:2px}
.rule{left:680px;top:540px;width:403px;height:1px;background:#222}
.social-badge{left:707px;top:572px;width:58px;height:64px;border-radius:10px;background:var(--badge)}
.social-link{font-family:"Arimo",sans-serif;font-weight:700;font-size:20px;color:var(--grey-light);text-decoration:none}

/* footer */
.footer{left:0;top:718px;width:1200px;height:50px;background:var(--black);color:var(--white);font-size:12.5px}
.footer a{position:absolute;top:15px;color:var(--white);text-decoration:none}
.copyright{position:absolute;right:147px;top:18px;font-size:12px}
</style>
</head>
<body>

<div class="abs backdrop-pattern" role="img" aria-label="Faint hexagon background pattern"></div>

<header>
  <div class="abs topbar"></div>
  <div class="abs brand-tab"></div>
  <div class="abs brand-name">Orbametric</div>
  <div class="abs login-field member">Member Login</div>
  <div class="abs login-field password">Password</div>
  <div class="abs login-link">Login <svg width="10" height="13" viewBox="0 0 10 13"><path d="M2 1l6 5.5L2 12" fill="none" stroke="#f15a22" stroke-width="2.4"/></svg></div>
  <nav class="abs nav">
    <a class="active" href="#">Home</a>
    <a href="#" style="left:577px">What?</a>
    <a href="#" style="left:647px">Why?</a>
    <a href="#" style="left:710px">Demo</a>
    <a href="#" style="left:771px">Reports</a>
    <a href="#" style="left:853px">Blog</a>
    <a href="#" style="left:910px">Pricing</a>
    <a href="#" style="left:985px">Contact Us</a>
  </nav>
</header>

<section class="hero">
  <div class="abs hero-mark" role="img" aria-label="Hexagon emblem decoration"></div>
  <div class="abs hero-kicker">Demand Generation &amp; Social Engagement</div>
  <h1 class="abs hero-title">Advocacy Marketing Platform</h1>
  <div class="abs btn-subscribe">Subscribe to<br>our newsletter
    <svg class="chev" width="30" height="47" viewBox="0 0 30 47"><path d="M4 0h10l14 23.5L14 47H4l14-23.5z" fill="#fff"/></svg>
  </div>
</section>

<section class="audiences">
  <div class="abs card" style="left:130px;top:244px">
    <div class="card-head" role="img" aria-label="Dark hexagon textured header"></div>
    <div class="card-icon"><svg width="22" height="32" viewBox="0 0 22 32"><rect x="6" y="1" width="10" height="18" rx="5" fill="#fff"/><path d="M2 14a9 9 0 0 0 18 0M11 23v6M6 30h10" fill="none" stroke="#fff" stroke-width="2.4"/></svg></div>
    <div class="card-title">ADVERTISERS</div>
    <ul><li>Create Polls and surveys</li><li>Create Competitions</li><li>Create B2B and B2C demand generation campaigns</li></ul>
    <div class="btn-register">Register<svg class="chev" width="22" height="34" viewBox="0 0 22 34"><path d="M2 0h8l10 17L10 34H2l10-17z" fill="#fff"/></svg></div>
  </div>

  <div class="abs card" style="left:407px;top:244px">
    <div class="card-head" role="img" aria-label="Dark hexagon textured header"></div>
    <div class="card-icon"><svg width="36" height="34" viewBox="0 0 36 34"><circle cx="18" cy="17" r="5" fill="#fff"/><circle cx="18" cy="3.5" r="3.5" fill="#fff"/><circle cx="4" cy="17" r="3.5" fill="#fff"/><circle cx="32" cy="17" r="3.5" fill="#fff"/><circle cx="26" cy="30" r="3.5" fill="#fff"/><path d="M18 4v13M4 17h28M18 17l8 13" stroke="#fff" stroke-width="2"/></svg></div>
    <div class="card-title">AFFILIATES</div>
    <ul><li>10% revenue share for tier one<br>referrals</li><li>5% revenue share for second<br>tier referrals</li><li>Real time reporting</li></ul>
    <div class="btn-register">Register<svg class="chev" width="22" height="34" viewBox="0 0 22 34"><path d="M2 0h8l10 17L10 34H2l10-17z" fill="#fff"/></svg></div>
  </div>

  <div class="abs card" style="left:130px;top:473px">
    <div class="card-head" role="img" aria-label="Dark hexagon textured header"></div>
    <div class="card-icon"><svg width="26" height="32" viewBox="0 0 26 32"><path d="M17 0L3 18h9l-4 14 15-19h-9z" fill="#fff"/></svg></div>
    <div class="card-title">ADVOCATES</div>
    <ul><li>Choose from both D2C or B2B<br>campaigns</li><li>Paid per lead</li><li>Full marketing tool kit</li></ul>
    <div class="btn-register">Register<svg class="chev" width="22" height="34" viewBox="0 0 22 34"><path d="M2 0h8l10 17L10 34H2l10-17z" fill="#fff"/></svg></div>
  </div>

  <div class="abs card" style="left:407px;top:473px">
    <div class="card-head" role="img" aria-label="Dark hexagon textured header"></div>
    <div class="card-icon"><svg width="34" height="26" viewBox="0 0 34 26"><path d="M12 5V2h10v3" fill="none" stroke="#fff" stroke-width="2.4"/><rect x="1" y="6" width="32" height="19" rx="2" fill="#fff"/></svg></div>
    <div class="card-title">AGENCIES</div>
    <ul><li>White label solution, upload logo or update CSS for full brand control</li><li>Build web forms to capture data</li><li>Cloudledger extension</li></ul>
    <div class="btn-register">Register<svg class="chev" width="22" height="34" viewBox="0 0 22 34"><path d="M2 0h8l10 17L10 34H2l10-17z" fill="#fff"/></svg></div>
  </div>
</section>

<section class="intro">
  <div class="abs intro-kicker">Generate Leads via</div>
  <h2 class="abs intro-head">Social Media Email and<br>Our Publisher Network...</h2>
  <p class="abs intro-copy">Our platform allows advertisers to easily create <em>surveys and lead generation campaigns</em> and publish them across the social web.</p>

  <div class="abs benefit" style="left:683px;top:404px;width:190px">Create branded campaign<br>landing pages without<br>IT or any technical skills<svg width="10" height="16" viewBox="0 0 10 16"><path d="M2 1l6 7-6 7" fill="none" stroke="#f15a22" stroke-width="3"/></svg></div>
  <div class="abs benefit" style="left:897px;top:403px;width:185px">Generate leads from<br>quillnest, chirvo and<br>pormbly.<svg width="10" height="16" viewBox="0 0 10 16"><path d="M2 1l6 7-6 7" fill="none" stroke="#f15a22" stroke-width="3"/></svg></div>
  <div class="abs benefit" style="left:683px;top:471px;width:200px">Engage with your audience<br>on the social web, survey<br>them for insights<svg width="10" height="16" viewBox="0 0 10 16"><path d="M2 1l6 7-6 7" fill="none" stroke="#f15a22" stroke-width="3"/></svg></div>
  <div class="abs benefit" style="left:902px;top:473px;width:185px">Reduce your sales<br>cycle by providing your<svg width="10" height="16" viewBox="0 0 10 16"><path d="M2 1l6 7-6 7" fill="none" stroke="#f15a22" stroke-width="3"/></svg></div>

  <div class="abs rule"></div>

  <div class="abs social-badge" role="img" aria-label="Social profiles badge"></div>
  <a class="abs social-link" href="#" style="left:782px;top:576px">quillnest</a>
  <a class="abs social-link" href="#" style="left:892px;top:576px">Tumbleway</a>
  <a class="abs social-link" href="#" style="left:785px;top:611px">chirvo</a>
  <a class="abs social-link" href="#" style="left:895px;top:611px">pormbly</a>
</section>

<footer class="abs footer">
  <a href="#" style="left:146px">About Us</a>
  <a href="#" style="left:215px">Contact Us</a>
  <a href="#" style="left:295px">Sitemap</a>
  <a href="#" style="left:359px">Privacy Policy</a>
  <span class="copyright">Copyright 2011 Orbametric.example. All rights reserved.</span>
</footer>

</body>
</html>
```